Sign Design

We already have a logo, but would like to design 2 x signs.
Sign 1:
Dimensions 1500mm wide x 2500m high.
Information to include on sign: - Clinic name and logo (attached)
- the word "DENTIST "
- Street number (which is 348)
Phone number (which is 6153 4097)

Sign 2:
Dimensions: 800mm wide x 600mm high

```html
<!DOCTYPE html>
<html lang="en">
<head>
<meta charset="utf-8">
<title>Kellbrook Dental Care – Dentist Signs</title>
<link rel="stylesheet" href="https://fonts.googleapis.com/css2?family=Archivo:wdth,wght@100..125,400..900&display=swap">
<style>
  :root {
    --backdrop: #323232;
    --sign-white: #ffffff;
    --forest: #116b38;
    --leaf: #1db32a;
    --pale-lime: #dff2b0;
    --lime: #a6dd4f;
    --grass: #8dd336;
    --deep-green: #0a9a0a;
  }
  html, body {
    margin: 0;
    padding: 0;
    overflow: hidden;
  }
  body {
    width: 1200px;
    height: 900px;
    background: var(--backdrop);
    position: relative;
    font-family: "Archivo", Arial, sans-serif;
  }
  .sign {
    position: absolute;
    background: var(--sign-white);
    overflow: hidden;
  }
  .sign-tall { left: 124px; top: 122px; width: 393px; height: 654px; }
  .sign-wide { left: 666px; top: 436px; width: 455px; height: 340px; }

  .decor-band {
    position: absolute;
    left: 0;
    right: 0;
    bottom: 0;
    background: linear-gradient(180deg, var(--pale-lime) 0%, var(--grass) 45%, var(--deep-green) 100%);
  }
  .sign-tall .decor-band { height: 190px; }
  .sign-wide .decor-band { height: 52px; }

  .decor-corner {
    position: absolute;
    left: 0;
    top: 0;
    width: 210px;
    height: 120px;
    background: linear-gradient(135deg, var(--leaf) 0%, var(--lime) 40%, rgba(223, 242, 176, 0) 72%);
  }

  .brand {
    position: absolute;
    display: flex;
    align-items: center;
    color: var(--forest);
    font-weight: 400;
    font-stretch: 100%;
  }
  .brand-dot {
    border-radius: 50%;
    background: var(--lime);
    flex: none;
  }
  .brand-name {
    line-height: 1;
    letter-spacing: -0.02em;
  }
  .brand-name span { display: block; text-align: right; }

  .sign-tall .brand { left: 32px; top: 46px; }
  .sign-tall .brand-dot { width: 80px; height: 80px; margin-right: 28px; }
  .sign-tall .brand-name { font-size: 42px; }
  .sign-tall .brand-name span + span { font-size: 22px; margin-top: 2px; }

  .sign-wide .brand { left: 220px; top: 22px; }
  .sign-wide .brand-dot { width: 50px; height: 50px; margin-right: 16px; }
  .sign-wide .brand-name { font-size: 26px; }
  .sign-wide .brand-name span + span { font-size: 15px; margin-top: 1px; }

  .title {
    position: absolute;
    left: 0; right: 0;
    margin: 0;
    text-align: center;
    color: var(--forest);
    font-weight: 800;
    font-stretch: 125%;
    letter-spacing: 0.05em;
    line-height: 1;
  }
  .sign-tall .title { top: 184px; font-size: 62px; }
  .sign-wide .title { top: 98px; font-size: 56px; }

  .detail {
    position: absolute;
    left: 0; right: 0;
    text-align: center;
    line-height: 1;
  }
  .detail-label {
    display: block;
    color: var(--leaf);
    font-weight: 600;
    letter-spacing: 0.02em;
  }
  .detail-value {
    display: inline-flex;
    align-items: center;
    color: var(--forest);
    font-weight: 800;
  }
  .detail-value svg { fill: var(--leaf); flex: none; }

  .sign-tall .street { top: 264px; }
  .sign-tall .street .detail-label { font-size: 16px; margin-bottom: 8px; }
  .sign-tall .street .detail-value { font-size: 50px; margin-left: -20px; }
  .sign-tall .street svg { width: 26px; height: 36px; margin-right: 8px; }

  .sign-tall .phone { top: 351px; }
  .sign-tall .phone .detail-label { font-size: 16px; margin-bottom: 12px; }
  .sign-tall .phone .detail-value { font-size: 50px; margin-left: -14px; }
  .sign-tall .phone svg { width: 40px; height: 40px; margin-right: 16px; }

  .sign-wide .street { top: 156px; }
  .sign-wide .street .detail-label { font-size: 13px; margin-bottom: 4px; }
  .sign-wide .street .detail-value { font-size: 40px; margin-left: -10px; }
  .sign-wide .street svg { width: 20px; height: 29px; margin-right: 6px; }

  .sign-wide .phone { top: 220px; }
  .sign-wide .phone .detail-label { font-size: 13px; margin-bottom: 6px; }
  .sign-wide .phone .detail-value { font-size: 40px; margin-left: -10px; }
  .sign-wide .phone svg { width: 32px; height: 32px; margin-right: 12px; }
</style>
</head>
<body>

<section class="sign sign-tall" aria-label="Tall dentist sign">
  <div class="decor-band" role="img" aria-label="Decorative green wave band"></div>

  <div class="brand">
    <span class="brand-dot"></span>
    <span class="brand-name"><span>Kellbrook</span><span>Dental Care</span></span>
  </div>

  <h1 class="title">DENTIST</h1>

  <div class="detail street">
    <span class="detail-label">Street Number</span>
    <span class="detail-value">
      <svg viewBox="0 0 24 34" aria-hidden="true"><path d="M12,0 C5.4,0 0,5.3 0,11.9 C0,20 12,34 12,34 C12,34 24,20 24,11.9 C24,5.3 18.6,0 12,0Z M12,17 A5.5,5.5 0 1 1 12,6 A5.5,5.5 0 1 1 12,17Z"/></svg>348
    </span>
  </div>

  <div class="detail phone">
    <span class="detail-label">Phone Number</span>
    <span class="detail-value">
      <svg viewBox="0 0 40 40" aria-hidden="true"><path d="M9,3 L14,3 L17,12 L13,16 C15,21 19,25 24,27 L28,23 L37,26 L37,31 C37,35 34,38 30,37 C16,35 5,24 3,10 C2,6 5,3 9,3Z"/><path d="M22,4 A14,14 0 0 1 36,18 L33,18 A11,11 0 0 0 22,7Z"/><path d="M22,10 A8,8 0 0 1 30,18 L27,18 A5,5 0 0 0 22,13Z"/></svg>6153 4097
    </span>
  </div>
</section>

<section class="sign sign-wide" aria-label="Wide dentist sign">
  <div class="decor-corner" role="img" aria-label="Decorative green wave corner"></div>
  <div class="decor-band" role="img" aria-label="Decorative green wave band"></div>

  <div class="brand">
    <span class="brand-dot"></span>
    <span class="brand-name"><span>Kellbrook</span><span>Dental Care</span></span>
  </div>

  <h2 class="title">DENTIST</h2>

  <div class="detail street">
    <span class="detail-label">Street Number</span>
    <span class="detail-value">
      <svg viewBox="0 0 24 34" aria-hidden="true"><path d="M12,0 C5.4,0 0,5.3 0,11.9 C0,20 12,34 12,34 C12,34 24,20 24,11.9 C24,5.3 18.6,0 12,0Z M12,17 A5.5,5.5 0 1 1 12,6 A5.5,5.5 0 1 1 12,17Z"/></svg>348
    </span>
  </div>

  <div class="detail phone">
    <span class="detail-label">Phone Number</span>
    <span class="detail-value">
      <svg viewBox="0 0 40 40" aria-hidden="true"><path d="M9,3 L14,3 L17,12 L13,16 C15,21 19,25 24,27 L28,23 L37,26 L37,31 C37,35 34,38 30,37 C16,35 5,24 3,10 C2,6 5,3 9,3Z"/><path d="M22,4 A14,14 0 0 1 36,18 L33,18 A11,11 0 0 0 22,7Z"/><path d="M22,10 A8,8 0 0 1 30,18 L27,18 A5,5 0 0 0 22,13Z"/></svg>6153 4097
    </span>
  </div>
</section>

</body>
</html>
```